Flyer Template Design

I have attached 4 files. I would like a design template that could be used across these documents so that they have a common look and feel. The content of the documents is tested and should not be changed significantly. The images can be changed. I have also attache our logo for color compatibility.
Updates

Need extra days to review

Target Market(s)

Wealthy Christian donors

Font styles to use
Serif
Sans Serif

```html
<!DOCTYPE html>
<html lang="en">
<head>
<meta charset="utf-8">
<title>The Harvest Fund — Flyer Series</title>
<link href="https://fonts.googleapis.com/css2?family=Philosopher&family=Open+Sans:wght@400;600;700&display=swap" rel="stylesheet">
<style>
:root{
  --blue:#4db6e4;
  --green:#5cb947;
  --ink:#2f2f2f;
  --text:#3a3a3a;
  --dark:#3b3b3b;
  --board:#8c8c8c;
  --paper:#ffffff;
}
*{box-sizing:border-box;margin:0;padding:0}
html,body{width:1200px;height:1200px;overflow:hidden}
body{background:var(--board);font-family:"Open Sans",Arial,sans-serif;color:var(--text);position:relative}
.flyer{position:absolute;width:352px;height:498px;background:var(--paper);overflow:hidden}
.flyer--commission{left:149px;top:102px}
.flyer--nations{left:674px;top:93px}
.flyer--coming{left:149px;top:656px}
.flyer--lap{left:674px;top:656px}
.header{position:absolute;left:0;top:0;width:352px;height:152px}
.brand{position:absolute;left:16px;top:38px;display:flex;align-items:center;gap:6px}
.brand__square{width:16px;height:16px;background:var(--green)}
.brand__name{font-family:"Open Sans",Arial,sans-serif;font-weight:600;font-size:10px;line-height:12px;color:var(--ink)}
.title{position:absolute;left:13px;font-family:"Philosopher",Georgia,serif;font-weight:400;font-size:25px;line-height:25px;letter-spacing:.2px}
.title .b{color:var(--blue)}
.title .g{color:var(--green)}
.content{position:absolute;left:13px;right:13px;font-size:4.5px;line-height:1.38}
.lead{font-weight:700;font-size:4.7px;color:var(--ink);margin-bottom:10px}
.cols{display:grid;grid-template-columns:1fr 1fr;column-gap:26px}
.h{color:var(--blue);font-size:5.4px;letter-spacing:.2px;text-transform:uppercase;margin:8px 0 4px}
p{margin-bottom:4px}
.strong{font-weight:700;color:var(--ink);font-size:5.4px;margin:8px 0 4px}
.mail{color:var(--blue);font-weight:600;font-size:5.4px}
.photo{border:1px solid var(--blue);height:48px;margin-bottom:4px}
.footer{position:absolute;left:0;bottom:0;width:352px;height:34px}
.footer__url{position:absolute;right:14px;bottom:7px;color:#fff;font-size:6px;font-weight:700;letter-spacing:2.2px}
</style>
</head>
<body>

<!-- Flyer: Finishing the Great Commission -->
<section class="flyer flyer--commission">
  <svg class="header" viewBox="0 0 352 152" preserveAspectRatio="none">
    <defs><linearGradient id="sky1" x1="0" y1="0" x2="1" y2="1"><stop offset="0" stop-color="#f4f5f6"/><stop offset=".6" stop-color="#c9cdd2"/><stop offset="1" stop-color="#8d8780"/></linearGradient></defs>
    <polygon role="img" aria-label="Photo of a robed figure holding an open book against a pale sky" fill="url(#sky1)" points="0,0 352,0 352,100 300,132 0,82"/>
    <polygon fill="var(--blue)" points="0,82 300,132 352,100 352,108 300,141 0,93"/>
    <polygon fill="var(--green)" points="0,93 300,141 352,108 352,118 300,152 0,106"/>
  </svg>
  <div class="brand"><span class="brand__square"></span><span class="brand__name">The Harvest Fund</span></div>
  <h1 class="title" style="top:154px"><span class="b">FINISHING</span><br><span class="g">THE GREAT COMMISSION</span></h1>
  <div class="content" style="top:212px">
    <p class="lead">Before Jesus ascended into heaven, He commanded his apostles, "Go and make disciples of all nations." For more than 2000 years the church has been working to fulfill this "Great Commission," and much has been accomplished. But now, for the first time in history, our generation has the real opportunity to finish the Great Commission in our lifetimes.</p>
    <div class="cols">
      <div>
        <div class="photo" role="img" aria-label="Row of portrait photos of people from different nations" style="background:linear-gradient(90deg,#6b4a36,#b2463a,#a0806a)"></div>
        <div class="h">It's about nations</div>
        <p>In the Bible, the word "nations" refers to people groups: groups of people who share a common ethnicity, culture, and language. So when Jesus said, "Go and make disciples of all nations," He was telling us to take the gospel to every people group on earth. Amazingly, there are about 12,000 of these people groups scattered throughout the world. And the Great Commission commands us to make disciples in every one of them.</p>
        <div class="h">Hastening his coming</div>
        <p>The Bible says that believers "ought to live holy and godly lives, looking for and hastening the coming of the day of God." It also says that day will not come until the gospel has been preached to "all nations." So how can hasten the day of his coming? By finishing the work he gave us to do: making disciples in all nations.</p>
        <div class="strong">You can make that happen.</div>
        <div class="strong" style="margin-top:6px;margin-bottom:1px">To learn more, email Martin Hale at</div>
        <div class="mail">mhale@harvestfund.org.</div>
      </div>
      <div>
        <div class="photo" role="img" aria-label="Row of portrait photos of people from different nations" style="background:linear-gradient(90deg,#c9a48a,#7a6a5c,#4a7a6a)"></div>
        <div class="h">Where do we stand?</div>
        <p>Today, there are still about 500 people groups who have never heard the gospel. Most of these groups are small and located in remote, difficult places. These remaining "unengaged" people groups have no known believers. But now that we know who and where these groups are, by God's grace it is possible that we can engage every one of them with the gospel within the next 3 years.</p>
        <div class="strong">In other words, we can finish the Great Commission!</div>
        <p>Partner with the Harvest Fund and finance the missionaries who are taking the gospel for the first time to those last remaining people groups. Your investment will "hasten the coming of the day of God" by accelerating the effort to make "disciples in every nation." In 2018, our partners helped take the gospel to 231 people groups in 35 countries.</p>
        <div class="strong">Join us as we invest to make disciples in<br>"all nations" by 2022</div>
      </div>
    </div>
  </div>
  <svg class="footer" viewBox="0 0 352 34" preserveAspectRatio="none">
    <polygon fill="var(--green)" points="0,2 352,12 352,14 0,14"/>
    <rect y="12" width="352" height="22" fill="var(--dark)"/>
  </svg>
  <span class="footer__url">www.harvestfund.org</span>
</section>

<!-- Flyer: God's Heart for the Nations -->
<section class="flyer flyer--nations">
  <svg class="header" viewBox="0 0 352 152" preserveAspectRatio="none">
    <defs><linearGradient id="sky2" x1="0" y1="0" x2="1" y2="1"><stop offset="0" stop-color="#f6f1e6"/><stop offset=".55" stop-color="#d9c7a8"/><stop offset="1" stop-color="#8a6a4c"/></linearGradient></defs>
    <polygon role="img" aria-label="Photo of a person with raised arms facing bright sunlight" fill="url(#sky2)" points="0,0 352,0 352,100 238,132 0,82"/>
    <polygon fill="var(--blue)" points="0,82 238,132 352,100 352,108 238,141 0,93"/>
    <polygon fill="var(--green)" points="0,93 238,141 352,108 352,118 238,152 0,106"/>
  </svg>
  <div class="brand"><span class="brand__square"></span><span class="brand__name">The Harvest Fund</span></div>
  <h1 class="title" style="top:154px"><span class="b">GOD HEART</span><br><span class="g">FOR THE NATIONS</span></h1>
  <div class="content" style="top:212px">
    <p class="lead" style="margin-bottom:6px">From beginning to end, the Bible reveals God's heart for "the nations."</p>
    <p><b>In Genesis</b>, God promises Abraham, "through your offspring all nations on the earth will be blessed."<br><b>The Psalms</b> prophesy that "all the nations you have made will come and worship before you, Lord."<br><b>In Isaiah</b>, God promises the Messiah, "I will make you a light to the nations, that my salvation may reach to the ends of the earth."<br><b>Daniel</b> sees "one like a son of man" who "was given authority, glory and sovereign power; all nations and peoples of every language worshiped him."</p>
    <div class="cols" style="grid-template-columns:86px 1fr;column-gap:12px;margin-top:6px">
      <div class="photo" role="img" aria-label="Grid of portrait photos of people from many nations" style="height:86px;background:linear-gradient(135deg,#8a5a40,#b03a3a,#4a6a8a,#a08060)"></div>
      <div>
        <p>In Matthew, Jesus commands his apostles to "Go and make disciples of all nations." And he links his return to the completion of that task, saying, "This gospel of the kingdom will be preached in the whole world as a testimony to all nations, and then the end will come."</p>
        <p style="margin-top:8px">In Revelation, John sees a "great multitude that no one could number, from every nation, from all tribes and peoples and languages, standing before the throne."</p>
        <p style="margin-top:8px">In the Bible, the word "nations" refers to people groups: groups of people who share a common ethnicity, culture, and language. Amazingly, there are more than 12,000 of these nations scattered around the world, and God has promised that every one of them will be included in His Kingdom.</p>
      </div>
    </div>
    <div class="cols" style="grid-template-columns:1fr 102px;column-gap:8px">
      <div>
        <div class="h">Finishing the task</div>
        <p>Today, there are still 500 nations who are not yet represented in God's Kingdom. No one has ever proclaimed the gospel to these "unengaged" people groups, and there are no believers among them. For these groups, God's promises have yet to be fulfilled. Most of these groups are small and located in remote, difficult places. But because we now know who and where they are, by God's grace it is possible that we can engage every one of them with the gospel within the next 3 years.</p>
      </div>
      <div class="photo" role="img" aria-label="Row of portrait photos of people from different nations" style="margin-top:8px;height:38px;background:linear-gradient(90deg,#7a6a5a,#5a4a3a,#9a7a9a,#e0e0e0)"></div>
    </div>
    <div class="cols" style="column-gap:14px">
      <div>
        <div class="strong" style="margin-top:4px">You can make that happen.</div>
        <div class="strong" style="margin-top:4px">Join us as we invest to make disciples in<br>"all nations" by 2022</div>
        <div class="strong" style="margin-top:6px;margin-bottom:1px">To learn more, email Martin Hale at</div>
        <div class="mail">mhale@harvestfund.org.</div>
      </div>
      <p style="margin-top:4px">Partner with the Harvest Fund and finance the missionaries who are taking the gospel for the first time to those last remaining people groups. Your investment will "hasten the coming of the day of God" by accelerating the effort to make "disciples in every nation." In 2018, our partners helped take the gospel to 231 people groups in 35 countries.</p>
    </div>
  </div>
  <svg class="footer" viewBox="0 0 352 34" preserveAspectRatio="none">
    <polygon fill="var(--green)" points="0,2 352,12 352,14 0,14"/>
    <rect y="12" width="352" height="22" fill="var(--dark)"/>
  </svg>
  <span class="footer__url">www.harvestfund.org</span>
</section>

<!-- Flyer: Hastening His Coming -->
<section class="flyer flyer--coming">
  <svg class="header" viewBox="0 0 352 152" preserveAspectRatio="none">
    <defs><linearGradient id="sky3" x1="0" y1="0" x2="0" y2="1"><stop offset="0" stop-color="#3e4a58"/><stop offset=".45" stop-color="#d9a64a"/><stop offset=".7" stop-color="#f1d27a"/><stop offset="1" stop-color="#4c5a2a"/></linearGradient></defs>
    <polygon role="img" aria-label="Photo of a sunrise over a green field under dramatic clouds" fill="url(#sky3)" points="0,0 352,0 352,100 210,132 0,82"/>
    <polygon fill="var(--blue)" points="0,82 210,132 352,100 352,108 210,141 0,93"/>
    <polygon fill="var(--green)" points="0,93 210,141 352,108 352,118 210,152 0,106"/>
  </svg>
  <div class="brand"><span class="brand__square"></span><span class="brand__name">The Harvest Fund</span></div>
  <h1 class="title" style="top:174px"><span class="b">HASTENING</span> <span class="g">HIS COMING</span></h1>
  <div class="content" style="top:208px">
    <p class="lead">In his second letter, the Apostle Peter asks, what kind of people should believers be? He answers, "We ought to live holy and godly lives, looking for and hastening the coming of the day of God." But how can we do that? How is it possible to hasten the coming of that day?</p>
    <div class="h" style="margin-top:0">"And then the end will come"</div>
    <p>When Jesus' disciples asked Him, "Tell us, what will be the sign of your coming and of the end of the age?"<br>He replied,<br>"This gospel of the kingdom will be preached in the whole world as a testimony to all nations, and then the end will come."</p>
    <div class="cols" style="margin-top:10px">
      <div>
        <p style="font-weight:700;color:var(--ink);font-size:5px">When will Jesus return?<br>He said, only after gospel has been preached to "all nations."</p>
        <p>In the Bible, the word "nations" refers to people groups: groups of people with common ethnicity, culture, and language. Amazingly, there are about 12,000 of these "nations" around the world—and Jesus commanded His church to preach the gospel to all of them! Today, there are still 500 people groups without a single believer. No one has ever gone to these remaining "unengaged" groups with the gospel. They do not know the name of Jesus.</p>
        <div class="strong" style="margin-top:12px">After 2000 years, isn't it time that they all heard?</div>
      </div>
      <div>
        <div class="h">Finishing the task</div>
        <p>So how can we "hasten the coming of the day of God?" By completing the work Jesus gave us to do! Jesus said He would not return until the gospel is preached to every nation, so that's what we need to do: take the gospel to all the groups that have never once heard it. Fortunately, we now know who these last groups are and where they are located, by God's grace it is possible that we can engage all of them with the gospel within the next 3 years.</p>
        <div class="strong" style="margin-top:12px">You can make that happen.</div>
      </div>
    </div>
    <p style="margin-top:6px">Partner with the Harvest Fund and finance the missionaries who are taking the gospel for the first time to those last remaining people groups. Your investment will "hasten the coming of the day of God" by accelerating the effort to make "disciples in every nation." In 2018, our partners helped take the gospel to 231 people groups in 35 countries.</p>
    <div class="cols" style="margin-top:12px">
      <div class="strong">Join us as we invest to make disciples in<br>"all nations" by 2022</div>
      <div><div class="strong" style="margin-bottom:1px">To learn more, email Martin Hale at</div><div class="mail">mhale@harvestfund.org.</div></div>
    </div>
  </div>
  <svg class="footer" viewBox="0 0 352 34" preserveAspectRatio="none">
    <polygon fill="var(--green)" points="0,2 352,12 352,14 0,14"/>
    <rect y="12" width="352" height="22" fill="var(--dark)"/>
  </svg>
  <span class="footer__url">www.harvestfund.org</span>
</section>

<!-- Flyer: The Final Lap -->
<section class="flyer flyer--lap">
  <svg class="header" viewBox="0 0 352 152" preserveAspectRatio="none">
    <defs><linearGradient id="sky4" x1="0" y1="0" x2="0" y2="1"><stop offset="0" stop-color="#dfe6ec"/><stop offset=".45" stop-color="#c8bca4"/><stop offset=".75" stop-color="#6a6e72"/><stop offset="1" stop-color="#d8d2c6"/></linearGradient></defs>
    <polygon role="img" aria-label="Photo of an ancient marble stadium with runners on the track" fill="url(#sky4)" points="0,0 352,0 352,100 212,132 0,82"/>
    <polygon fill="var(--blue)" points="0,82 212,132 352,100 352,108 212,141 0,93"/>
    <polygon fill="var(--green)" points="0,93 212,141 352,108 352,118 212,152 0,106"/>
  </svg>
  <div class="brand"><span class="brand__square"></span><span class="brand__name">The Harvest Fund</span></div>
  <h1 class="title" style="top:166px"><span class="b">THE FINAL</span> <span class="g">LAP</span></h1>
  <div class="content" style="top:202px">
    <p class="lead" style="margin-bottom:8px">Every four years, the great city marathon is run through the streets of the host city. The final lap, though, is always run in the main stadium. At the end of the race, the runners burst into the stadium for the final lap, and the crowd explodes in celebration of a long race well run.</p>
    <div class="cols" style="column-gap:18px">
      <div>
        <div class="h" style="margin-top:0">The finish line</div>
        <p>Jesus himself defined the finish line when he said, "This gospel of the kingdom will be preached in the whole world as a testimony to all nations, and then the end will come."</p>
        <p style="font-weight:700;color:var(--ink);font-size:5px;margin-top:6px">When will the race end?<br>Jesus said, when the gospel has been proclaimed to "all nations."</p>
        <div class="h">Sprinting to the finish</div>
        <p>In his second letter, the Apostle Peter instructs believers "to hasten the coming of the day of God." As the end of the race draws near, he's saying, we should sprint toward the finish line, striving to finish the race as quickly as we can.</p>
        <div class="strong" style="font-size:4.8px">You can be part of the sprint to the finish.</div>
        <p>Partner with the Harvest Fund and finance the missionaries who are taking the gospel for the first time to those last remaining people groups. Your investment will "hasten the coming of the day of God" by accelerating the effort to make "disciples in every nation." In 2018, our partners helped take the gospel to 231 people groups in 35 countries.</p>
        <div class="strong" style="margin-top:8px">Join us as we invest to make disciples in<br>"all nations" by 2022</div>
        <div class="strong" style="margin-top:8px;margin-bottom:1px">To learn more, email Martin Hale at</div>
        <div class="mail">mhale@harvestfund.org.</div>
      </div>
      <div>
        <p>In the Bible, the word "nations" refers to people groups: groups of people who share a common ethnicity, culture, and language. Amazingly, there are about 12,000 of these "nations" around the world—and Jesus commanded us to make disciples in all of them!<br>Today, there are still about 500 people groups around the world who have never heard the gospel.<br>Most of these remaining groups are small and located in remote, difficult places. But now that we know who and where they are, by God's grace it is possible for us to engage every one of them with the gospel within the next 3 years.</p>
        <div class="strong" style="font-size:4.8px">In other words, after a long race, we're on the final lap!</div>
        <div class="photo" role="img" aria-label="Photo of a sprinter crossing the finish line on a red track" style="height:112px;margin-top:10px;background:linear-gradient(160deg,#b8503c,#8a3a2e 60%,#c46a4c)"></div>
      </div>
    </div>
  </div>
  <svg class="footer" viewBox="0 0 352 34" preserveAspectRatio="none">
    <polygon fill="var(--green)" points="0,2 352,12 352,14 0,14"/>
    <rect y="12" width="352" height="22" fill="var(--dark)"/>
  </svg>
  <span class="footer__url">www.harvestfund.org</span>
</section>

</body>
</html>
```